Lena Corvel Business Card

I need a business card that reflects my current website: itslenacorvel.com and screenshot attached. If we keep the color scheme of the site and sample card below that would be ideal. The business card should include the information on the attached sample cards.

Industry/Entity Type

Business

```html
<!DOCTYPE html>
<html lang="en">
<head>
<meta charset="utf-8">
<title>Lena Corvel Business Card</title>
<link rel="stylesheet" href="https://fonts.googleapis.com/css2?family=Caveat+Brush&family=Dancing+Script:wght@600&family=Oswald:wght@300&display=swap">
<style>
  :root {
    --backdrop: #e6e6e2;
    --card: #ffffff;
    --card-shade: #eeeeee;
    --teal: #4fbfa3;
    --teal-deep: #3aa98f;
    --ink: #1c1c1c;
    --ink-soft: #444444;
  }
  * { box-sizing: border-box; margin: 0; padding: 0; }
  html, body {
    width: 1200px; height: 800px; overflow: hidden;
    background: var(--backdrop);
  }
  .stage {
    position: relative; width: 1200px; height: 800px;
    display: flex; align-items: center; justify-content: center; gap: 40px;
  }
  .card {
    position: relative; width: 540px; height: 308px;
    background: linear-gradient(135deg, var(--card) 0%, var(--card) 55%, var(--card-shade) 100%);
    box-shadow: 0 6px 18px rgba(0,0,0,.18);
    overflow: hidden;
  }
  .band-top {
    position: absolute; left: 0; right: 0; top: 7px; height: 11px;
    background: var(--teal);
  }
  .band-bottom {
    position: absolute; left: 0; right: 0; bottom: 6px; height: 34px;
    background: linear-gradient(var(--teal) 0 18px, var(--card) 18px 22px, var(--teal-deep) 22px 34px);
  }
  .signature {
    position: absolute;
    font-family: "Caveat Brush", cursive;
    color: var(--ink);
    white-space: nowrap;
    line-height: 1;
  }
  .signature .prefix { font-size: 22px; margin-right: 6px; }
  .signature .name { font-size: 44px; }
  .tagline {
    position: absolute;
    font-family: "Dancing Script", cursive;
    font-weight: 600;
    font-size: 11.5px;
    color: var(--ink-soft);
    white-space: nowrap;
  }
  .card--front .signature { left: 170px; top: 120px; }
  .card--front .tagline { left: 150px; top: 172px; }
  .card--back .signature { left: 48px; top: 156px; }
  .card--back .tagline { left: 30px; top: 208px; }
  .contacts {
    position: absolute; left: 300px; top: 66px;
    list-style: none;
    font-family: "Oswald", sans-serif; font-weight: 300;
    font-size: 14px; color: var(--ink-soft);
  }
  .contacts li {
    display: flex; align-items: center; gap: 20px;
    height: 26px;
  }
  .contacts svg { width: 14px; height: 14px; fill: var(--teal); flex: none; }
  .social-dot {
    width: 12px; height: 12px; border-radius: 50%;
    background: var(--teal); flex: none; margin: 0 1px;
  }
</style>
</head>
<body>
<main class="stage">
  <section class="card card--front" aria-label="Card front">
    <div class="band-top"></div>
    <p class="signature"><span class="prefix">its</span><span class="name">Lena Corvel</span></p>
    <p class="tagline">Brand Curator - Digital Storyteller - Social Entrepreneur</p>
    <div class="band-bottom"></div>
  </section>

  <section class="card card--back" aria-label="Card back">
    <div class="band-top"></div>
    <ul class="contacts">
      <li>
        <svg viewBox="0 0 24 24" aria-hidden="true"><path d="M6.6 10.8a15 15 0 0 0 6.6 6.6l2.2-2.2a1 1 0 0 1 1-.25 11.4 11.4 0 0 0 3.6.57 1 1 0 0 1 1 1V20a1 1 0 0 1-1 1A17 17 0 0 1 3 4a1 1 0 0 1 1-1h3.5a1 1 0 0 1 1 1 11.4 11.4 0 0 0 .57 3.6 1 1 0 0 1-.25 1z"/></svg>
        <span>240.555.0142</span>
      </li>
      <li>
        <svg viewBox="0 0 24 24" aria-hidden="true"><path d="M2 5h20v14H2z M3.5 6.5 12 13l8.5-6.5" fill="none" stroke="var(--teal)" stroke-width="2.4"/></svg>
        <span>me@lenacorvel.com</span>
      </li>
      <li>
        <svg viewBox="0 0 24 24" aria-hidden="true"><circle cx="12" cy="12" r="9.5" fill="none" stroke="var(--teal)" stroke-width="2.4"/><path d="M2.5 12h19M12 2.5c3.2 3 3.2 16 0 19M12 2.5c-3.2 3-3.2 16 0 19" fill="none" stroke="var(--teal)" stroke-width="1.8"/></svg>
        <span>www.itslenacorvel.com</span>
      </li>
      <li>
        <span class="social-dot" aria-hidden="true"></span>
        <span>@itslenacorvel</span>
      </li>
    </ul>
    <p class="signature"><span class="prefix">its</span><span class="name">Lena Corvel</span></p>
    <p class="tagline">Brand Curator - Digital Storyteller - Social Entrepreneur</p>
    <div class="band-bottom"></div>
  </section>
</main>
</body>
</html>
```